Business Card Design

We need business cards designed incorporating our graphics/logo already used on our trucks. We are a small construction company that does everything from building new homes, additions, Kitchens, Baths, Decks, Hardwood Floors/Tile, all phases of construction. No job is too small. We pride ourselves on True Craftmanship/Customer Satisfaction, its what truly separates us from everyone else.

Industry/Entity Type

Construction

Contact Information for Business Card

Maple Ridge Renovations Lic#27KP51986400
342 51st Avenue Lakeview Cove NJ 08117
(555)731-2948 Email: info@mapleridgeexample.com
Paul Vandermolen

```html
<!DOCTYPE html>
<html lang="en">
<head>
<meta charset="utf-8">
<title>Maple Ridge Renovations – Business Card</title>
<link rel="stylesheet" href="https://fonts.googleapis.com/css2?family=Archivo+Black&family=Molengo&display=swap">
<style>
  :root {
    --page: #ecebe8;
    --sky-top: #5fa9d6;
    --sky-bottom: #a6d7f0;
    --sand: #d9a56f;
    --sand-deep: #c8925c;
    --ink: #1a1a1a;
    --brand: #2a2318;
    --white: #ffffff;
    --figure-tone: #4d6aa8;
  }
  * { box-sizing: border-box; margin: 0; padding: 0; }
  html, body { width: 1200px; height: 1200px; overflow: hidden; background: var(--page); }
  .canvas { position: relative; width: 1200px; height: 1200px; }

  .card {
    position: absolute; left: 120px; width: 960px; height: 549px;
    overflow: hidden; box-shadow: 0 6px 18px rgba(0,0,0,.18);
  }
  .card--front { top: 34px; }
  .card--back { top: 617px; }
  .card__bg { position: absolute; inset: 0; width: 100%; height: 100%; }

  .brand-name {
    position: absolute; font-family: "Archivo Black", "Arial Black", sans-serif;
    color: var(--brand); letter-spacing: 3px; text-transform: uppercase; line-height: 1;
    text-align: center;
  }
  .card--front .brand-name { left: 40px; top: 40px; width: 700px; font-size: 62px; }
  .card--front .brand-name span { display: block; }
  .card--front .brand-name span + span { margin-top: 24px; }

  .mascot-art {
    position: absolute; right: 40px; top: 215px; width: 210px; height: 175px;
    border-radius: 10px;
    background: linear-gradient(180deg, var(--figure-tone), var(--sand-deep));
  }

  .services { position: absolute; left: 90px; top: 335px; list-style: none; }
  .services li {
    position: relative; padding-left: 34px; margin-bottom: 12px;
    font-family: "Archivo Black", "Arial Black", sans-serif; font-size: 38px; line-height: 1.1;
    color: var(--white); letter-spacing: 1px; text-transform: uppercase;
    text-shadow: 2px 2px 0 var(--ink), -1px -1px 0 var(--ink), 1px -1px 0 var(--ink), -1px 1px 0 var(--ink);
  }
  .services li::before {
    content: ""; position: absolute; left: 0; top: 13px; width: 18px; height: 18px;
    border-radius: 50%; background: var(--ink);
  }

  .card--back .brand-name { left: 0; top: 40px; width: 960px; font-size: 64px; }
  .card--back .brand-name span { display: block; }
  .card--back .brand-name span + span { margin-top: 22px; }

  .holder {
    position: absolute; left: 50px; top: 350px; width: 340px;
    font-family: "Molengo", sans-serif; font-size: 38px; color: var(--ink);
  }
  .divider { position: absolute; left: 400px; top: 300px; width: 2px; height: 190px; background: #5a4632; }
  .contact {
    position: absolute; left: 440px; top: 300px; list-style: none;
    font-family: "Molengo", sans-serif; font-size: 28px; color: var(--ink); line-height: 1.2;
  }
  .contact li { display: flex; gap: 14px; margin-bottom: 14px; }
  .contact svg { flex: none; width: 24px; height: 28px; margin-top: 3px; fill: var(--ink); }
</style>
</head>
<body>
<main class="canvas">

  <section class="card card--front" aria-label="Card front">
    <svg class="card__bg" viewBox="0 0 960 549" preserveAspectRatio="none" aria-hidden="true">
      <defs>
        <linearGradient id="skyFront" x1="0" y1="0" x2="0" y2="1">
          <stop offset="0" stop-color="var(--sky-top)"/>
          <stop offset="1" stop-color="var(--sky-bottom)"/>
        </linearGradient>
      </defs>
      <rect width="960" height="549" fill="url(#skyFront)"/>
      <path d="M0 300 C120 290 220 300 300 285 C360 272 380 250 420 255 C500 265 560 240 640 225 C760 200 860 190 960 180 L960 549 L0 549 Z"
            fill="var(--sand)"/>
      <path d="M0 300 C120 290 220 300 300 285 C360 272 380 250 420 255 C500 265 560 240 640 225 C760 200 860 190 960 180"
            fill="none" stroke="var(--ink)" stroke-width="5"/>
    </svg>
    <h1 class="brand-name"><span>Maple Ridge</span><span>Renovations</span></h1>
    <div class="mascot-art" role="img" aria-label="Illustration of two cartoon builders in hard hats beside a signpost"></div>
    <ul class="services">
      <li>Remodeling</li>
      <li>Decks</li>
      <li>Additions</li>
    </ul>
  </section>

  <section class="card card--back" aria-label="Card back">
    <svg class="card__bg" viewBox="0 0 960 549" preserveAspectRatio="none" aria-hidden="true">
      <defs>
        <linearGradient id="skyBack" x1="0" y1="0" x2="0" y2="1">
          <stop offset="0" stop-color="var(--sky-top)"/>
          <stop offset="1" stop-color="var(--sky-bottom)"/>
        </linearGradient>
      </defs>
      <rect width="960" height="549" fill="var(--sand)"/>
      <rect width="960" height="250" fill="url(#skyBack)"/>
    </svg>
    <h2 class="brand-name"><span>Maple Ridge</span><span>Renovations</span></h2>
    <p class="holder">Paul Vandermolen</p>
    <div class="divider"></div>
    <ul class="contact">
      <li>
        <svg viewBox="0 0 24 28" aria-hidden="true"><path d="M12 0C5.4 0 1 4.6 1 10.5 1 18 12 28 12 28s11-10 11-17.5C23 4.6 18.6 0 12 0zm0 15a4.5 4.5 0 1 1 0-9 4.5 4.5 0 0 1 0 9z"/></svg>
        <span>#27KP51986400 342 51st Avenue<br>Lakeview Cove NJ 08117</span>
      </li>
      <li>
        <svg viewBox="0 0 24 28" aria-hidden="true"><path d="M5 2l4 0 2 6-3 2c1.5 3.5 4 6 7 7.5l2-3 6 2v4c0 1.5-1 2.5-2.5 2.5C10 23 2 15 2 5 2 3 3 2 5 2z"/></svg>
        <span>(555)731-2948</span>
      </li>
      <li>
        <svg viewBox="0 0 24 28" aria-hidden="true"><path d="M1 7h22v15H1zM2.5 8.5 12 16l9.5-7.5" stroke="var(--sand)" stroke-width="1.6"/></svg>
        <span>info@mapleridgeexample.com</span>
      </li>
    </ul>
  </section>

</main>
</body>
</html>
```